Tall Pine Advertising ad for electronic billboard

I need an ad made for an electronic billboard (13 feet x 26 Feet)(1024 x 480)
We own the billboard and want an ad to draw in customers.
Phone number: 250-317-4056
email: tbrask@tallpineadvertising.ca
I was thinking a Tall Pine swimming in the background with our email, phone number and company name Tall Pine in grey sitting above Advertising in white.
It can't be to busy, the less busy the ad is the better.

Target Market(s)

we are located in a oil patch town

Industry/Entity Type

Electronic

Requirements
Must have
• phone number
• your ad here
• email
• company name
Nice to have
• a shark

```html
<!DOCTYPE html>
<html lang="en">
<head>
<meta charset="utf-8">
<title>Tall Pine Advertising – Your Ad Here</title>
<link rel="stylesheet" href="https://fonts.googleapis.com/css2?family=Montserrat:wght@500;600&display=swap">
<style>
  :root {
    --page-bg: #e9edf1;
    --sky-top: #e6f0ec;
    --sky-bottom: #d5e6e2;
    --surface-line: #1f6f7e;
    --water-top: #3a9aa8;
    --water-mid: #1f7b8a;
    --water-deep: #0f4f5c;
    --accent-orange: #f49a1f;
    --text-light: #ffffff;
    --text-soft: #dcefee;
    --logo-bg: #ffffff;
    --logo-ink: #2d3f8f;
  }
  * { margin: 0; padding: 0; box-sizing: border-box; }
  html, body {
    width: 1200px;
    height: 926px;
    overflow: hidden;
    background: var(--page-bg);
  }
  body {
    display: flex;
    align-items: center;
    justify-content: center;
    font-family: "Montserrat", sans-serif;
  }
  .billboard-ad {
    position: relative;
    width: 1120px;
    height: 525px;
    overflow: hidden;
    background: linear-gradient(180deg, var(--water-top) 0%, var(--water-mid) 45%, var(--water-deep) 100%);
  }
  .above-surface {
    position: absolute;
    left: 0; top: 0;
    width: 100%;
    height: 150px;
    background: linear-gradient(180deg, var(--sky-top), var(--sky-bottom));
    border-bottom: 4px solid var(--surface-line);
  }
  .headline {
    position: absolute;
    color: var(--accent-orange);
    font-weight: 500;
    font-size: 82px;
    letter-spacing: 4px;
    line-height: 1;
  }
  .headline-your-ad { left: 70px; top: 70px; }
  .headline-here { left: 680px; top: 118px; font-size: 90px; }
  .shark-illustration {
    position: absolute;
    left: 370px;
    top: 120px;
    width: 460px;
    height: 220px;
    border-radius: 50%;
    background: radial-gradient(ellipse at 45% 50%, rgba(120, 200, 215, 0.75) 0%, rgba(70, 160, 180, 0.45) 45%, rgba(31, 123, 138, 0) 72%);
  }
  .contact-block {
    position: absolute;
    left: 75px;
    top: 320px;
    color: var(--text-light);
  }
  .company-name {
    font-weight: 600;
    font-size: 21px;
    letter-spacing: 1.5px;
    text-transform: uppercase;
  }
  .contact-email {
    margin-top: 6px;
    font-weight: 500;
    font-size: 18px;
    color: var(--text-soft);
  }
  .phone-row {
    display: flex;
    align-items: center;
    gap: 22px;
    margin-top: 24px;
  }
  .phone-icon { width: 58px; height: 58px; }
  .phone-number {
    font-weight: 500;
    font-size: 62px;
    letter-spacing: 2px;
  }
  .brand-badge {
    position: absolute;
    right: 28px;
    bottom: 24px;
    width: 118px;
    height: 112px;
    border-radius: 10px;
    background: var(--logo-bg);
    display: flex;
    align-items: center;
    justify-content: center;
    text-align: center;
    padding: 10px;
  }
  .brand-badge-name {
    color: var(--logo-ink);
    font-weight: 600;
    font-size: 15px;
    line-height: 1.25;
  }
</style>
</head>
<body>
  <main class="billboard-ad">
    <div class="above-surface"></div>
    <div class="shark-illustration" role="img" aria-label="Shark swimming just beneath the water surface with its dorsal fin breaking through"></div>
    <h1 class="headline headline-your-ad">YOUR AD</h1>
    <p class="headline headline-here">HERE</p>

    <section class="contact-block">
      <p class="company-name">Tall Pine Advertising</p>
      <p class="contact-email">tbrask@tallpineadvertising.ca</p>
      <div class="phone-row">
        <svg class="phone-icon" viewBox="0 0 58 58" aria-hidden="true">
          <circle cx="29" cy="29" r="26.5" fill="none" stroke="#ffffff" stroke-width="3"/>
          <path d="M21 16c1.5-1 3-.6 3.8.8l2.6 4.6c.7 1.3.4 2.6-.7 3.4l-1.8 1.3c1 2.8 3.3 5.8 6 7.6l1.7-1.3c1.1-.8 2.5-.8 3.5.1l4 3.4c1.2 1 1.3 2.6.2 3.8l-1.6 1.8c-1.6 1.8-4.2 2.2-6.5 1-6.6-3.6-11.6-9.9-13.6-17-.7-2.5.2-4.8 2.4-6.1z" fill="#ffffff"/>
        </svg>
        <span class="phone-number">250-317-4056</span>
      </div>
    </section>

    <div class="brand-badge">
      <span class="brand-badge-name">Tall Pine Advertising</span>
    </div>
  </main>
</body>
</html>
```